TIVARELCAP web-presence redisign

We would like to have our existing web-presence redesigned. Have a look at www.tivarel.ch (please use explorer). To the existing 11 pages we would add one more.

```html
<!DOCTYPE html>
<html lang="de">
<head>
<meta charset="utf-8">
<title>TIVARELCAP Zahnarztpraxis</title>
<link rel="stylesheet" href="https://fonts.googleapis.com/css2?family=Open+Sans:wght@400;600;700;800&display=swap">
<style>
:root{
  --orange:#f7a600;
  --orange-dark:#e08e00;
  --ink:#333333;
  --muted:#777777;
  --line:#dddddd;
  --paper:#ffffff;
  --footer:#3b3b3b;
  --social:#2f6fb5;
  --hero-bg:#eef1f4;
}
*{margin:0;padding:0;box-sizing:border-box}
html,body{width:828px;height:1200px;overflow:hidden;background:var(--paper);font-family:"Open Sans",Arial,sans-serif;color:var(--ink)}
.page{position:relative;width:828px;height:1200px}

/* header */
.site-header{height:90px;display:flex;justify-content:space-between;align-items:center;padding:0 28px}
.brand{display:flex;align-items:center;gap:10px}
.brand-mark{width:34px;height:34px;background:var(--orange)}
.brand-name{font-size:26px;font-weight:800;color:var(--orange);line-height:1}
.brand-sub{font-size:14px;font-weight:600;color:var(--muted);margin-top:3px}
.contact{text-align:right;width:260px}
.contact-note{font-size:9px;line-height:12px;color:var(--muted)}
.contact-phone{display:flex;justify-content:flex-end;align-items:center;gap:6px;font-size:22px;font-weight:600;color:var(--ink);margin-top:4px}

/* nav */
.main-nav{height:28px;background:linear-gradient(var(--orange),var(--orange-dark));display:flex;padding:0 28px}
.main-nav a{color:#fff;text-decoration:none;font-size:11px;font-weight:600;line-height:28px;padding:0 22px;border-right:1px solid rgba(255,255,255,.35)}
.main-nav a:first-child{padding-left:0}
.main-nav a:last-child{border-right:none}

/* hero */
.hero{position:relative;height:268px;background:var(--hero-bg);overflow:hidden}
.hero-photo{position:absolute;left:40px;top:0;width:420px;height:268px;background:radial-gradient(circle at 45% 45%,#f4e0cf 0%,#e8d3c3 35%,#eef1f4 75%)}
.hero-copy{position:absolute;left:500px;top:46px;width:270px}
.hero-kicker{font-size:20px;font-weight:700;color:var(--ink)}
.hero-title{font-size:31px;font-weight:800;color:var(--orange-dark);line-height:1.1;margin-bottom:12px}
.hero-text{font-size:12px;line-height:16px;color:var(--muted);margin-bottom:16px}
.btn{display:inline-block;background:var(--orange);color:#fff;font-size:11px;font-weight:700;padding:10px 18px;text-decoration:none}
.hero-arrow{position:absolute;top:120px}

/* welcome */
.welcome{text-align:center;padding:20px 60px 0}
.welcome h1{font-size:17px;font-weight:700;margin-bottom:6px}
.divider{width:300px;height:1px;background:var(--line);margin:0 auto 10px}
.welcome p{font-size:9.5px;line-height:14px;color:var(--muted)}
.welcome .sign{margin-top:16px;font-size:9.5px}

/* cards */
.cards{display:flex;justify-content:space-between;padding:26px 40px 0}
.card{width:236px;height:296px;border:1px solid var(--line);background:#fff;display:flex;flex-direction:column;align-items:center}
.card h2{font-size:15px;font-weight:700;margin:12px 0 10px}
.card-photo{width:112px;height:112px;border-radius:50%;border:4px solid #fff;box-shadow:0 0 0 1px var(--line);position:relative;z-index:1;background:radial-gradient(circle at 50% 40%,#f1dccb,#b9cfe0)}
.card-body{margin-top:-56px;padding-top:66px;width:100%;flex:1;background:var(--orange);text-align:center;color:#fff;font-size:9.5px;line-height:13px;padding-left:20px;padding-right:20px}
.card-more{display:block;background:#fff;color:var(--ink);font-size:9px;font-weight:700;width:100%;text-align:center;padding:9px 0;border-top:1px solid var(--line)}

/* team */
.team{position:relative;padding-top:30px;text-align:center}
.team h2{font-size:24px;font-weight:700;margin-bottom:6px}
.team .divider{width:700px;margin-bottom:14px}
.team-list{display:flex;justify-content:center;gap:26px}
.member{width:108px}
.member-photo{width:98px;height:98px;margin:0 auto 6px;border-radius:50%;border:4px solid #fff;box-shadow:0 0 0 1px var(--line);background:radial-gradient(circle at 50% 40%,#efd6c2,#c9b3a2)}
.member-name{font-size:9px;font-weight:600}
.member-role{font-size:9px;color:var(--muted)}
.team-arrow{position:absolute;top:128px}

/* footer */
.site-footer{position:absolute;left:40px;right:40px;bottom:18px;height:76px;background:var(--footer);color:#fff;padding:14px 20px}
.footer-nav{display:flex;gap:20px;font-size:10px;font-weight:600}
.footer-copy{font-size:8px;color:#bbb;margin-top:10px}
.social{position:absolute;right:20px;top:18px;display:flex;gap:8px}
.social span{width:24px;height:24px;background:var(--social)}
</style>
</head>
<body>
<div class="page">
  <header class="site-header">
    <div class="brand">
      <span class="brand-mark"></span>
      <div>
        <div class="brand-name">TIVARELCAP</div>
        <div class="brand-sub">Zahnarztpraxis</div>
      </div>
    </div>
    <div class="contact">
      <p class="contact-note">One of our representatives will happily contact you within 24 hours. For urgent needs call us at</p>
      <div class="contact-phone">
        <svg width="18" height="18" viewBox="0 0 24 24"><path fill="#e08e00" d="M6.6 10.8a15 15 0 0 0 6.6 6.6l2.2-2.2c.3-.3.7-.4 1-.2 1.1.4 2.3.6 3.6.6.6 0 1 .4 1 1V20c0 .6-.4 1-1 1A17 17 0 0 1 3 4c0-.6.4-1 1-1h3.5c.6 0 1 .4 1 1 0 1.3.2 2.5.6 3.6.1.3 0 .7-.2 1z"/></svg>
        +41 (0) 44 000 12 34
      </div>
    </div>
  </header>

  <nav class="main-nav">
    <a href="#">HOME</a><a href="#">ZAHNMEDIZIN</a><a href="#">DENTALHYGIENE</a><a href="#">TEAM</a><a href="#">TESTIMONIAL</a><a href="#">KONTAKT</a>
  </nav>

  <section class="hero">
    <div class="hero-photo" role="img" aria-label="Smiling woman holding a green apple"></div>
    <div class="hero-copy">
      <div class="hero-kicker">HIGH QUALITY OF</div>
      <div class="hero-title">DENTAL CARE</div>
      <p class="hero-text">Lorem ipsum dolor sit amet conse ctetur adipiscing elit, sed do eiusmod tempor incididunt ut labore et dolore magna aliqua. Ut enim ad minim veniam.</p>
      <a class="btn" href="#">READ MORE</a>
    </div>
    <svg class="hero-arrow" style="left:10px" width="14" height="22" viewBox="0 0 14 22"><path d="M11 2 3 11l8 9" fill="none" stroke="#444" stroke-width="3"/></svg>
    <svg class="hero-arrow" style="right:10px" width="14" height="22" viewBox="0 0 14 22"><path d="m3 2 8 9-8 9" fill="none" stroke="#444" stroke-width="3"/></svg>
  </section>

  <section class="welcome">
    <h1>Herzlich willkommen in unserer neuen Praxis.</h1>
    <div class="divider"></div>
    <p>Es ist unser Ziel, Ihr Wohlbefinden zu steigern: Sie sollen die Schönheit des Alltags mit gesunden Zähnen geniessen<br>und in jeder Situation herzhaft lachen können.</p>
    <p class="sign">Ihre Zahnärztin, Dr. med. dent. Livia Marent-Hofer</p>
  </section>

  <section class="cards">
    <article class="card">
      <h2>OUR AIM</h2>
      <div class="card-photo" role="img" aria-label="Portrait of the dentist"></div>
      <div class="card-body">Aenean nonummy hendrerit mauris. Phasellus porta. Fusce suscipit varius mi. Cum sociis natoque penatibus et magnis.</div>
      <span class="card-more">READ MORE</span>
    </article>
    <article class="card">
      <h2>OUR MISSION</h2>
      <div class="card-photo" role="img" aria-label="Patient during a dental check-up"></div>
      <div class="card-body">Aenean nonummy hendrerit mauris. Phasellus porta. Fusce suscipit varius mi. Cum sociis natoque penatibus et magnis.</div>
      <span class="card-more">READ MORE</span>
    </article>
    <article class="card">
      <h2>OUR VISION</h2>
      <div class="card-photo" role="img" aria-label="Child being treated in the dental chair"></div>
      <div class="card-body">Aenean nonummy hendrerit mauris. Phasellus porta. Fusce suscipit varius mi. Cum sociis natoque penatibus et magnis.</div>
      <span class="card-more">READ MORE</span>
    </article>
  </section>

  <section class="team">
    <h2>Meet Our Team</h2>
    <div class="divider"></div>
    <div class="team-list">
      <div class="member"><div class="member-photo" role="img" aria-label="Portrait of the chief dentist"></div><div class="member-name">Dr. Livia Marent-Hofer</div><div class="member-role">Chief Dentist</div></div>
      <div class="member"><div class="member-photo" role="img" aria-label="Portrait of a dentist"></div><div class="member-name">Dr. Sara Wendl</div><div class="member-role">Dentist</div></div>
      <div class="member"><div class="member-photo" role="img" aria-label="Portrait of a dental hygienist"></div><div class="member-name">Mira Selden</div><div class="member-role">Dental Hygienist</div></div>
      <div class="member"><div class="member-photo" role="img" aria-label="Portrait of a dental hygienist"></div><div class="member-name">Nadja Brugger</div><div class="member-role">Dental Hygienist</div></div>
      <div class="member"><div class="member-photo" role="img" aria-label="Portrait of a dental assistant"></div><div class="member-name">Elena Corvin</div><div class="member-role">Dental Assistant</div></div>
    </div>
    <svg class="team-arrow" style="left:20px" width="24" height="24" viewBox="0 0 24 24"><circle cx="12" cy="12" r="12" fill="#f7a600"/><path d="M14 7l-5 5 5 5" fill="none" stroke="#fff" stroke-width="2.5"/></svg>
    <svg class="team-arrow" style="right:20px" width="24" height="24" viewBox="0 0 24 24"><circle cx="12" cy="12" r="12" fill="#f7a600"/><path d="M10 7l5 5-5 5" fill="none" stroke="#fff" stroke-width="2.5"/></svg>
  </section>

  <footer class="site-footer">
    <div class="footer-nav"><span>Home</span><span>Zahnmedizin</span><span>Dentalhygiene</span><span>Team</span><span>Kontakt</span></div>
    <p class="footer-copy">© 2016, All Rights Reserved. Tivarelcap, Zahnarztpraxis</p>
    <div class="social"><span></span><span></span></div>
  </footer>
</div>
</body>
</html>
```